Flyer for American Indian Elders on Dementia Warning Signs

We need a flyer designed for older adults who are American Indian or Alaska Native (in the U.S.).

Ideally, the flyer should complement the colors of our logos. The project logo and our organization logo are attached to the brief.

When people see the flyer we want them to feel that it represents their culture, is warm, and professional but relatable to older adults and people who have limited incomes.

I have attached an earlier draft of the document we designed ourselves BUT we want different and better.

It is for older adults who have trouble reading so:
1. you must use a font that is 11.5 points or larger
2. Do not put text over complex pictures or use shading with words
3. You can use a serif font for the heading, but should use san serif for the body text
4. There should be good contrast between the font color and background

Please do not use any images that include a head dress or pictures of American Indian people or things that are very traditional or "token" imagery.

We need to save a small space under the call out box/ somewhere on the flyer for other people to add their logo once they download.

Let us know if you have questions or need additional information.

Target Market(s)

Older American Indian people

Font styles to use
Serif
Sans Serif

Requirements
Must have
• Easy to read for older adults
Should not have
• indian headdress

```html
<!DOCTYPE html>
<html lang="en">
<head>
<meta charset="utf-8">
<title>10 Signs of Thinking or Memory Changes</title>
<link href="https://fonts.googleapis.com/css2?family=Merriweather:wght@700;900&family=Open+Sans:wght@400;600;700;800&display=swap" rel="stylesheet">
<style>
:root{
  --page:#eeeeee;
  --paper:#ffffff;
  --maroon:#8c1f2a;
  --teal:#1f6f78;
  --teal-dark:#164f58;
  --teal-soft:#2b8893;
  --ink:#2a2a2a;
  --muted:#555555;
  --sand:#d9b48a;
}
*{box-sizing:border-box;margin:0;padding:0}
html,body{width:1200px;height:3296px;overflow:hidden;background:var(--page)}
body{position:relative;font-family:"Open Sans",Arial,sans-serif;color:var(--ink)}
.flyer{position:absolute;width:960px;height:1480px;background:var(--paper);padding:36px 40px;transform-origin:top left}
.flyer--first{left:120px;top:20px}
.flyer--second{left:60px;top:1580px;transform:scale(1.125)}

.masthead{display:flex;align-items:center;gap:18px;height:140px}
.brand{width:170px;display:flex;align-items:center;gap:10px}
.brand__dot{width:26px;height:26px;border-radius:50%;background:var(--teal)}
.brand__name{font-weight:800;font-size:22px;color:var(--teal);line-height:1.1}
.signs-badge{width:92px;height:118px;background:var(--maroon);color:#fff;display:flex;flex-direction:column;align-items:center;justify-content:center;font-family:"Merriweather",Georgia,serif}
.signs-badge__num{font-size:50px;font-weight:900;line-height:1}
.signs-badge__word{font-size:20px;font-weight:700;letter-spacing:2px}
.headline{font-family:"Merriweather",Georgia,serif;font-weight:900;color:var(--maroon);line-height:1.12}
.headline__top{font-size:27px;display:block}
.headline__main{font-size:40px;display:block}

.intro{display:flex;height:220px;margin-top:14px;background:var(--teal-dark)}
.intro__text{flex:1;padding:22px 26px;color:#fff;font-size:15px;line-height:1.5}
.intro__text p+p{margin-top:12px}
.intro__photo{width:360px;background:linear-gradient(160deg,#8fb6c9 0%,#c9a27a 55%,#7d5a3c 100%)}

.ask{margin-top:24px;font-size:25px;font-weight:800;color:var(--maroon)}

.body{display:flex;gap:28px;margin-top:18px}
.signs{flex:1;list-style:none}
.sign{display:flex;gap:14px;min-height:76px;margin-bottom:6px}
.sign__num{flex:none;width:36px;height:36px;border-radius:50%;background:var(--maroon);color:#fff;font-weight:800;font-size:15px;display:flex;align-items:center;justify-content:center}
.sign__title{font-weight:800;font-size:15px;color:var(--teal-dark);line-height:1.3}
.sign__detail{font-size:13px;color:var(--muted);line-height:1.35;margin-top:2px}
.sign__detail li{margin-left:16px}

.aside{width:310px;flex:none}
.facts{background:var(--teal);color:#fff;padding:18px 20px}
.fact{display:flex;gap:14px;padding:16px 0;border-bottom:1px solid rgba(255,255,255,.35)}
.fact:last-child{border-bottom:none}
.fact__icon{flex:none;width:44px;height:44px;border-radius:8px;background:var(--teal-dark);display:flex;align-items:center;justify-content:center}
.fact__text{font-size:16px;line-height:1.4}
.partner{margin-top:22px;text-align:center}
.partner__name{font-weight:800;font-size:19px;color:var(--teal);line-height:1.2}
.partner__note{margin-top:10px;font-size:12px;color:var(--muted);line-height:1.4}
.partner__link{display:block;margin-top:6px;font-weight:800;font-size:16px;color:var(--maroon)}
.logo-space{margin-top:18px;height:70px;border:2px dashed #c7c7c7}

.footnote{position:absolute;left:40px;right:40px;bottom:30px;font-size:12px;color:var(--muted);text-align:center;line-height:1.4}
</style>
</head>
<body>

<article class="flyer flyer--first">
  <header class="masthead">
    <div class="brand"><span class="brand__dot"></span><span class="brand__name">Elder Mind</span></div>
    <div class="signs-badge"><span class="signs-badge__num">10</span><span class="signs-badge__word">SIGNS</span></div>
    <h1 class="headline"><span class="headline__top">OF THINKING OR MEMORY CHANGES</span><span class="headline__main">THAT MIGHT BE DEMENTIA</span></h1>
  </header>
  <section class="intro">
    <div class="intro__text">
      <p>As we get older, we may slow down a bit. This is a normal part of aging. Changes in memory or thinking that make it harder to get through the day are not a normal part of aging. These may be early signs of dementia.</p>
      <p>Because American Indian and Alaska Native people have a high risk of dementia, it is important to know the warning signs.</p>
    </div>
    <div class="intro__photo" role="img" aria-label="Photo of two elders smiling together outdoors"></div>
  </section>
  <h2 class="ask">Do you have any of these 10 signs? If so, talk to your doctor.</h2>
  <div class="body">
    <ol class="signs">
      <li class="sign"><span class="sign__num">01</span><div><p class="sign__title">Memory loss that affects your daily life. You may:</p><ul class="sign__detail"><li>Forget events or important dates</li><li>Repeat yourself</li><li>Rely more often on lists or sticky notes to remember things</li></ul></div></li>
      <li class="sign"><span class="sign__num">02</span><div><p class="sign__title">Trouble planning or solving problems. You may have a harder time</p><ul class="sign__detail"><li>Paying bills</li><li>Cooking recipes you have used for years</li></ul></div></li>
      <li class="sign"><span class="sign__num">03</span><div><p class="sign__title">Get confused about the time, date, or where you are.</p></div></li>
      <li class="sign"><span class="sign__num">04</span><div><p class="sign__title">Daily tasks are getting harder, including:</p><ul class="sign__detail"><li>Driving</li><li>Making a grocery list or going shopping</li></ul></div></li>
      <li class="sign"><span class="sign__num">05</span><div><p class="sign__title">Trouble with how your eyesight and thinking work together that gets worse. This includes:</p><ul class="sign__detail"><li>Tripping, falls, or problems with your balance</li><li>Spilling or dropping things more</li></ul></div></li>
      <li class="sign"><span class="sign__num">06</span><div><p class="sign__title">New trouble talking or writing.</p><p class="sign__detail">You have a hard time finding the words you want to say. For example, you may say "that thing on your wrist that tells time" instead of "watch."</p></div></li>
      <li class="sign"><span class="sign__num">07</span><div><p class="sign__title">Lose and cannot find things. For example, you:</p><ul class="sign__detail"><li>Can't find the coffee pot that you use every day</li><li>Might put your car keys in the freezer</li></ul></div></li>
      <li class="sign"><span class="sign__num">08</span><div><p class="sign__title">Notice changes in mood or personality, such as being:</p><ul class="sign__detail"><li>Easily mad or sad in everyday situations</li><li>More fearful (scared) or suspicious (not trusting)</li></ul></div></li>
      <li class="sign"><span class="sign__num">09</span><div><p class="sign__title">Act different and make poor choices. This may make you more likely to:</p><ul class="sign__detail"><li>Spend money you do not have or be a scam victim</li><li>Stop washing up regularly or pay less attention to how you look</li><li>Forget to take care of your pet</li></ul></div></li>
      <li class="sign"><span class="sign__num">10</span><div><p class="sign__title">Pull away from friends and family because it is harder to keep up</p><p class="sign__detail">You may not want to do things you used to enjoy, like sporting events, church, music, or sewing.</p></div></li>
    </ol>
    <aside class="aside">
      <div class="facts">
        <div class="fact"><span class="fact__icon"><svg width="26" height="26" viewBox="0 0 26 26"><circle cx="9" cy="8" r="4" fill="#fff"/><circle cx="18" cy="8" r="4" fill="#fff"/><rect x="3" y="14" width="20" height="9" rx="4" fill="#fff"/></svg></span><p class="fact__text">American Indian and Alaska Native people have a high risk of dementia.</p></div>
        <div class="fact"><span class="fact__icon"><svg width="26" height="26" viewBox="0 0 26 26"><circle cx="13" cy="13" r="10" fill="none" stroke="#fff" stroke-width="2.5"/><path d="M13 7v6l4 3" stroke="#fff" stroke-width="2.5" fill="none"/></svg></span><p class="fact__text">Big changes in memory or thinking that make it hard to get through the day are not a normal part of aging.</p></div>
        <div class="fact"><span class="fact__icon"><svg width="26" height="26" viewBox="0 0 26 26"><rect x="10" y="3" width="6" height="20" fill="#fff"/><rect x="3" y="10" width="20" height="6" fill="#fff"/></svg></span><p class="fact__text">People with one or more of these 10 signs should talk to their doctor to find the cause. It is not always dementia.</p></div>
        <div class="fact"><span class="fact__icon"><svg width="26" height="26" viewBox="0 0 26 26"><path d="M5 13l5 5 11-11" stroke="#fff" stroke-width="3" fill="none"/></svg></span><p class="fact__text">Early dementia diagnosis gives you a chance to get care and plan your future.</p></div>
      </div>
      <div class="partner">
        <p class="partner__name">Northern Circle Brain Health Center</p>
        <p class="partner__note">To learn more about the warning signs of dementia in American Indian and Alaska Native people, visit:</p>
        <span class="partner__link">www.northcirclebrain.org</span>
        <span class="partner__link">www.healthagency.gov/aging</span>
      </div>
    </aside>
  </div>
  <p class="footnote">Adapted from public resources on healthy aging. Made in partnership with local tribal health programs. Funding supported by a federal public health grant.</p>
</article>

<article class="flyer flyer--second">
  <header class="masthead">
    <div class="brand"><span class="brand__dot"></span><span class="brand__name">Elder Mind</span></div>
    <div class="signs-badge"><span class="signs-badge__num">10</span><span class="signs-badge__word">SIGNS</span></div>
    <h1 class="headline"><span class="headline__top">OF THINKING OR MEMORY CHANGES</span><span class="headline__main">THAT MIGHT BE DEMENTIA</span></h1>
  </header>
  <section class="intro">
    <div class="intro__text">
      <p>As we get older, we may slow down a bit. This is a normal part of aging. Changes in memory or thinking that make it harder to get through the day are not a normal part of aging. These may be early signs of dementia.</p>
      <p>Because American Indian and Alaska Native people have a high risk of dementia, it is important to know the warning signs.</p>
    </div>
    <div class="intro__photo" role="img" aria-label="Photo of two elders smiling together outdoors"></div>
  </section>
  <h2 class="ask">Do you have any of these 10 signs? If so, talk to your doctor.</h2>
  <div class="body">
    <ol class="signs">
      <li class="sign"><span class="sign__num">01</span><div><p class="sign__title">Memory loss that affects your daily life. You may:</p><ul class="sign__detail"><li>Forget events or important dates</li><li>Repeat yourself</li><li>Rely more often on lists or sticky notes to remember things</li></ul></div></li>
      <li class="sign"><span class="sign__num">02</span><div><p class="sign__title">Trouble planning or solving problems. You may have a harder time</p><ul class="sign__detail"><li>Paying bills</li><li>Cooking recipes you have used for years</li></ul></div></li>
      <li class="sign"><span class="sign__num">03</span><div><p class="sign__title">Get confused about the time, date, or where you are.</p></div></li>
      <li class="sign"><span class="sign__num">04</span><div><p class="sign__title">Daily tasks are getting harder, including:</p><ul class="sign__detail"><li>Driving</li><li>Making a grocery list or going shopping</li></ul></div></li>
      <li class="sign"><span class="sign__num">05</span><div><p class="sign__title">Trouble with how your eyesight and thinking work together that gets worse. This includes:</p><ul class="sign__detail"><li>Tripping, falls, or problems with your balance</li><li>Spilling or dropping things more</li></ul></div></li>
      <li class="sign"><span class="sign__num">06</span><div><p class="sign__title">New trouble talking or writing.</p><p class="sign__detail">You have a hard time finding the words you want to say. For example, you may say "that thing on your wrist that tells time" instead of "watch."</p></div></li>
      <li class="sign"><span class="sign__num">07</span><div><p class="sign__title">Lose and cannot find things. For example, you:</p><ul class="sign__detail"><li>Can't find the coffee pot that you use every day</li><li>Might put your car keys in the freezer</li></ul></div></li>
      <li class="sign"><span class="sign__num">08</span><div><p class="sign__title">Notice changes in mood or personality, such as being:</p><ul class="sign__detail"><li>Easily mad or sad in everyday situations</li><li>More fearful (scared) or suspicious (not trusting)</li></ul></div></li>
      <li class="sign"><span class="sign__num">09</span><div><p class="sign__title">Act different and make poor choices. This may make you more likely to:</p><ul class="sign__detail"><li>Spend money you do not have or be a scam victim</li><li>Stop washing up regularly or pay less attention to how you look</li><li>Forget to take care of your pet</li></ul></div></li>
      <li class="sign"><span class="sign__num">10</span><div><p class="sign__title">Pull away from friends and family because it is harder to keep up</p><p class="sign__detail">You may not want to do things you used to enjoy, like sporting events, church, music, or sewing.</p></div></li>
    </ol>
    <aside class="aside">
      <div class="facts">
        <div class="fact"><span class="fact__icon"><svg width="26" height="26" viewBox="0 0 26 26"><circle cx="9" cy="8" r="4" fill="#fff"/><circle cx="18" cy="8" r="4" fill="#fff"/><rect x="3" y="14" width="20" height="9" rx="4" fill="#fff"/></svg></span><p class="fact__text">American Indian and Alaska Native people have a high risk of dementia.</p></div>
        <div class="fact"><span class="fact__icon"><svg width="26" height="26" viewBox="0 0 26 26"><circle cx="13" cy="13" r="10" fill="none" stroke="#fff" stroke-width="2.5"/><path d="M13 7v6l4 3" stroke="#fff" stroke-width="2.5" fill="none"/></svg></span><p class="fact__text">Big changes in memory or thinking that make it hard to get through the day are not a normal part of aging.</p></div>
        <div class="fact"><span class="fact__icon"><svg width="26" height="26" viewBox="0 0 26 26"><rect x="10" y="3" width="6" height="20" fill="#fff"/><rect x="3" y="10" width="20" height="6" fill="#fff"/></svg></span><p class="fact__text">People with one or more of these 10 signs should talk to their doctor to find the cause. It is not always dementia.</p></div>
        <div class="fact"><span class="fact__icon"><svg width="26" height="26" viewBox="0 0 26 26"><path d="M5 13l5 5 11-11" stroke="#fff" stroke-width="3" fill="none"/></svg></span><p class="fact__text">Early dementia diagnosis gives you a chance to get care and plan your future.</p></div>
      </div>
      <div class="partner">
        <p class="partner__name">Northern Circle Brain Health Center</p>
        <p class="partner__note">To learn more about the warning signs of dementia in American Indian and Alaska Native people, visit:</p>
        <span class="partner__link">www.northcirclebrain.org</span>
        <span class="partner__link">www.healthagency.gov/aging</span>
      </div>
    </aside>
  </div>
  <p class="footnote">Adapted from public resources on healthy aging. Made in partnership with local tribal health programs. Funding supported by a federal public health grant.</p>
</article>

</body>
</html>
```